Ridgecrest Career Institute needs a unique tri-fold brochure design

I need a tri-fold brochure for my vocational school. We provide Nursing Assistant, Home Healthcare Aide & Phlebotomy classes at our centers and 50 programs online. The theme for our brochure and logo is Opening New Doors. I have all the text for the brochure and simples of brochures that I Like. I want the brochure to stand out and represent high quality and success. I also want the brochure to be easy to read. Yes, I'm also open to different ideas and concepts. lol
Updates

The logo and a sample of the text are now available with my brief.

Thanks,

Reg

Thanks to all the designers who took on the project and emailed me directly! If you have not replied to the invite, email me at, rmolvern47@quillpost.net

Thanks again, 
Reg 

Hello All,

Payment for the project is now GUARANTEED! Feel free to email me directly at rmolvern47@quillpost.net or you can post your first draft on my page. Fyi... full content for the brochure is only available upon request.

Thanks,

Reg

Target Market(s)

18-55 years old, but the vast majority are between the age of 24-45

Industry/Entity Type

School

Requirements
Must have
• Pictures of people in scrubs of all ages.
Should not have
• pictures of people in business wear.

```html
<!DOCTYPE html>
<html lang="en">
<head>
<meta charset="utf-8">
<title>Ridgecrest Career Institute – Tri-fold Brochure</title>
<link rel="stylesheet" href="https://fonts.googleapis.com/css2?family=Source+Sans+3:ital,wght@0,400;0,600;0,700;1,600;1,700&family=Varela+Round&display=swap">
<style>
  :root {
    --page-bg: #cfdde3;
    --panel-top: #f6fafd;
    --panel-bottom: #dcecf6;
    --blue: #1a9ad6;
    --blue-light: #8fd0ef;
    --blue-pale: #e6f3fa;
    --navy: #233a8c;
    --red: #d22a2a;
    --text: #3b4650;
    --white: #ffffff;
  }
  * { box-sizing: border-box; margin: 0; padding: 0; }
  html, body { width: 1200px; height: 1057px; overflow: hidden; }
  body {
    background: var(--page-bg);
    font-family: "Source Sans 3", Arial, sans-serif;
    color: var(--text);
    position: relative;
  }
  .panel {
    position: absolute;
    top: 178px;
    height: 700px;
    background: linear-gradient(180deg, var(--panel-top) 0%, var(--panel-bottom) 100%);
    overflow: hidden;
    box-shadow: 0 6px 18px rgba(40, 70, 90, 0.25);
  }
  .panel-cover { left: 20px; width: 290px; }
  .inside-spread { position: absolute; left: 340px; top: 178px; width: 840px; height: 700px; box-shadow: 0 6px 18px rgba(40, 70, 90, 0.25); }
  .inside-spread .panel { top: 0; width: 280px; box-shadow: none; }
  .panel-about { left: 0; }
  .panel-courses { left: 280px; border-left: 1px solid rgba(0,0,0,0.06); }
  .panel-cna { left: 560px; border-left: 1px solid rgba(0,0,0,0.06); }

  .swoosh { position: absolute; left: 0; width: 100%; pointer-events: none; }
  .swoosh-top { top: 0; height: 90px; }
  .swoosh-bottom { bottom: 0; height: 120px; }

  /* cover */
  .brand { position: absolute; top: 92px; left: 0; width: 100%; text-align: center; }
  .brand-mark { display: inline-block; width: 18px; height: 18px; border-radius: 50%; background: var(--navy); vertical-align: middle; margin-right: 6px; }
  .brand-name { font-weight: 700; font-size: 15px; color: var(--navy); vertical-align: middle; }
  .brand-rule { width: 150px; height: 1px; background: var(--blue); margin: 14px auto 0; }
  .headline { position: absolute; top: 152px; width: 100%; text-align: center; font-family: "Varela Round", Arial, sans-serif; font-weight: 400; }
  .headline-main { display: block; font-size: 40px; color: var(--red); line-height: 1; }
  .headline-sub { display: block; font-size: 26px; color: var(--navy); line-height: 1.2; }
  .headline-rule { width: 150px; height: 1px; background: var(--blue); margin: 8px auto 0; }
  .benefits { position: absolute; top: 262px; left: 24px; right: 14px; list-style: none; }
  .benefits li { font-weight: 700; font-style: italic; font-size: 13.5px; color: var(--blue); margin-bottom: 7px; display: flex; align-items: center; }
  .benefits svg { width: 12px; height: 12px; margin-right: 6px; flex: none; }
  .cover-photo {
    position: absolute; top: 410px; left: 0; width: 100%; height: 200px;
    background: linear-gradient(160deg, #e9d5cb 0%, #c98a9a 45%, #8fb3d6 100%);
  }
  .cover-contact { position: absolute; bottom: 16px; left: 18px; color: var(--white); font-size: 12.5px; line-height: 1.25; z-index: 2; }
  .cover-contact strong { font-size: 16px; font-weight: 600; }

  /* inside */
  .section-title { font-weight: 700; font-size: 14px; color: var(--red); text-transform: uppercase; letter-spacing: 0.3px; }
  .course-title { font-weight: 700; font-size: 12.5px; color: var(--red); text-transform: uppercase; margin: 10px 0 4px; }
  .copy { font-size: 11.5px; line-height: 1.5; }
  .copy + .copy { margin-top: 8px; }
  .indent { text-indent: 14px; }
  .panel-body { position: absolute; left: 24px; right: 20px; z-index: 2; }
  .panel-about .panel-body { top: 30px; }
  .panel-about .section-title { margin-bottom: 6px; }
  .panel-about .section-title.second { margin-top: 18px; }
  .callout { margin-top: 18px; font-weight: 700; font-size: 17px; line-height: 1.2; color: var(--red); }
  .panel-courses .panel-body { top: 44px; }
  .panel-cna .panel-body { top: 110px; }

  .team-photo {
    position: absolute; left: 280px; top: 470px; width: 560px; height: 230px;
    background: linear-gradient(180deg, rgba(220,236,246,0) 0%, #e4e9ee 22%, #b9c6d8 68%, #7f9ccb 100%);
  }
</style>
</head>
<body>

  <section class="panel panel-cover" aria-label="Front cover">
    <svg class="swoosh swoosh-top" viewBox="0 0 290 90" preserveAspectRatio="none" aria-hidden="true">
      <path d="M0 0 H290 V30 C200 70 90 20 0 55 Z" fill="var(--blue)"/>
      <path d="M0 55 C90 20 200 70 290 30 V45 C200 85 90 40 0 70 Z" fill="var(--blue-light)" opacity="0.7"/>
    </svg>

    <div class="brand">
      <span class="brand-mark" aria-hidden="true"></span><span class="brand-name">Ridgecrest Career Institute</span>
      <div class="brand-rule"></div>
    </div>

    <h1 class="headline">
      <span class="headline-main">Opening</span>
      <span class="headline-sub">New Doors</span>
      <span class="headline-rule" style="display:block"></span>
    </h1>

    <ul class="benefits">
      <li><svg viewBox="0 0 12 12"><path d="M1 6.5 L4.5 10 L11 2" fill="none" stroke="var(--red)" stroke-width="2"/></svg>Affordable &amp; Quality Education</li>
      <li><svg viewBox="0 0 12 12"><path d="M1 6.5 L4.5 10 L11 2" fill="none" stroke="var(--red)" stroke-width="2"/></svg>Fast &amp; Efficient Training</li>
      <li><svg viewBox="0 0 12 12"><path d="M1 6.5 L4.5 10 L11 2" fill="none" stroke="var(--red)" stroke-width="2"/></svg>High Paying Jobs &amp; Rewarding Careers</li>
      <li><svg viewBox="0 0 12 12"><path d="M1 6.5 L4.5 10 L11 2" fill="none" stroke="var(--red)" stroke-width="2"/></svg>State Certified Caregivers &amp; Highly Rated Employers</li>
      <li><svg viewBox="0 0 12 12"><path d="M1 6.5 L4.5 10 L11 2" fill="none" stroke="var(--red)" stroke-width="2"/></svg>Training Facility &amp; Community</li>
    </ul>

    <div class="cover-photo" role="img" aria-label="Group photo of smiling healthcare workers of all ages in scrubs"></div>

    <svg class="swoosh swoosh-bottom" viewBox="0 0 290 120" preserveAspectRatio="none" aria-hidden="true">
      <path d="M0 40 C90 0 200 10 290 45 V120 H0 Z" fill="var(--blue-light)"/>
      <path d="M0 60 C100 25 200 30 290 60 V120 H0 Z" fill="var(--blue)"/>
    </svg>
    <p class="cover-contact">Enroll Online:<br>ridgecrestcareer.com<br>Or Call: <strong>555-014-0188</strong></p>
  </section>

  <div class="inside-spread">
    <section class="panel panel-about" aria-label="About us">
      <div class="panel-body">
        <h2 class="section-title">About Us</h2>
        <p class="copy">At Ridgecrest Career Institute your success is our focus. Whether you want to challenge the CNA state exam, or simply boost your healthcare or computer skills, our professional instructors go above and beyond to help you succeed.</p>
        <h2 class="section-title second">Why Choose Us</h2>
        <p class="copy">Small classes, flexible schedules and hands-on clinical practice prepare you for the workforce. Our graduates are proud members of our community.</p>
        <p class="callout">We are here to help you move forward!</p>
      </div>
      <svg class="swoosh swoosh-bottom" viewBox="0 0 280 120" preserveAspectRatio="none" aria-hidden="true">
        <path d="M0 30 C80 70 200 60 280 20 V120 H0 Z" fill="var(--blue-light)"/>
        <path d="M0 60 C90 95 200 85 280 55 V120 H0 Z" fill="var(--blue)"/>
      </svg>
    </section>

    <section class="panel panel-courses" aria-label="Our courses">
      <div class="panel-body">
        <h2 class="section-title">Our Courses</h2>
        <h3 class="course-title">1. Home Health Aide</h3>
        <p class="copy indent">Home Health Aides provide health care services in a homes setting. Their clients include the elderly or people with long-term illnesses or disabilities. This course will provide all the clinical skills and knowledge to perform at your best in the workforce. Our courses are taught by certified and experienced professionals and licensed by the State Board of Career Education.</p>
        <h3 class="course-title">2. Phlebotomy Technician</h3>
        <p class="copy indent">Phlebotomist draws the patient's blood for use in medical tests so that physicians are able to properly diagnose illnesses and diseases.</p>
        <p class="copy indent">According to phlebcareerpay.com, a well-trained &amp; certified technician can expect between $20,000 to $35,000 annually. A Phlebotomy Technician can work in a Hospital, clinical laboratory, blood banks, research facilities, insurance companies and private physician's offices.</p>
      </div>
    </section>

    <section class="panel panel-cna" aria-label="More courses">
      <svg class="swoosh swoosh-top" viewBox="0 0 280 90" preserveAspectRatio="none" aria-hidden="true">
        <path d="M0 0 H280 V70 C200 40 110 20 30 40 C60 15 150 5 0 0 Z" fill="var(--blue)"/>
        <path d="M20 50 C110 20 200 40 280 75 V88 C200 55 110 38 20 50 Z" fill="var(--blue-light)"/>
      </svg>
      <div class="panel-body">
        <h3 class="course-title">3. Certified Nursing Assistant (CNA)</h3>
        <p class="copy indent">A Certified Nursing Assistant (CNA) provides care for patients that might include assistance with daily living activities such as bathing, dressing and feeding. In addition, certified nursing assistants provide vital support to the nurses and doctors with which the work.</p>
        <p class="copy indent">CNAs work in a variety of healthcare settings in our region. Hospitals, nursing homes, assisted living facilities, Alzheimer's units, and home health environments, just to name a few.</p>
        <h3 class="course-title">4. Online Diploma Pathways</h3>
        <p class="copy indent">Career-credentialed certificate programs for in-demand careers, such as Early Childhood Education, Transportation Services, Criminal Justice, Office Management, and Homeland Security.</p>
      </div>
    </section>

    <div class="team-photo" role="img" aria-label="Photo of a row of healthcare professionals in white coats and scrubs, one holding a clipboard"></div>
  </div>

</body>
</html>
```